Business Card Design Project

We require business cards to be produced with the following design
http://files.pixelvault-demo.net/img/50329/84172/84172_2093548_50329_image.jpg
Rather than bright meadow, please use Vantelo as the comapny name.
Please also use the following contact details:
1.
Daniel Overbeck
Entrepreneur
07423158871
doverbeck@vantelo-demo.com
2.
Tom Ashworth
Founder
07539402217
tashworth@vantelo-demo.com
Please add:
Facebook favicion facebook.com/vantelo
Linked in favicon linkedin/danieloverbeck
Skype favicon doverbeck
Linked in favicon linkedin/thomasashworth
Skype favicon thomasashworth
Google Plus favicon tomashworth@mailbox-demo.net
To the back

```html
<!DOCTYPE html>
<html lang="en">
<head>
<meta charset="utf-8">
<title>Vantelo Business Card</title>
<link rel="stylesheet" href="https://fonts.googleapis.com/css2?family=Montserrat:wght@400;500;700&display=swap">
<style>
  :root {
    --backdrop: #4b4a4a;
    --card-dark: #2f2b2b;
    --card-light: #ffffff;
    --brand-red: #e3161f;
    --ink-dark: #3a3636;
    --text-light: #ffffff;
    --text-muted: #b9b5b5;
  }
  * { margin: 0; padding: 0; box-sizing: border-box; }
  html, body {
    width: 1200px;
    height: 900px;
    overflow: hidden;
    background: var(--backdrop);
    font-family: "Montserrat", sans-serif;
  }
  .card-sheet {
    width: 1200px;
    height: 900px;
    display: flex;
    align-items: center;
    justify-content: center;
    gap: 80px;
  }
  .card {
    position: relative;
    width: 320px;
    height: 560px;
    box-shadow: 0 14px 30px rgba(0, 0, 0, 0.35);
  }
  .card--front { background: var(--card-light); }
  .card--back { background: var(--card-dark); color: var(--text-light); }

  .brand {
    display: flex;
    flex-direction: column;
    align-items: flex-start;
    gap: 8px;
  }
  .brand__mark {
    width: 34px;
    height: 34px;
    background: var(--brand-red);
  }
  .brand__name {
    font-weight: 700;
    font-size: 20px;
    letter-spacing: 0.5px;
    text-transform: uppercase;
  }
  .card--front .brand {
    position: absolute;
    left: 150px;
    bottom: 58px;
  }
  .card--front .brand__name { color: var(--ink-dark); font-size: 24px; }
  .card--back .brand {
    position: absolute;
    left: 30px;
    top: 46px;
  }
  .card--back .brand__name { color: var(--text-light); }

  .holder {
    position: absolute;
    left: 30px;
    top: 170px;
  }
  .holder__name {
    font-weight: 500;
    font-size: 24px;
    letter-spacing: 0.3px;
  }
  .holder__role {
    margin-top: 6px;
    font-size: 9px;
    letter-spacing: 1.5px;
    color: var(--text-muted);
    text-transform: uppercase;
  }

  .contacts {
    position: absolute;
    left: 58px;
    top: 380px;
    list-style: none;
    font-size: 11px;
    line-height: 1;
  }
  .contacts li {
    display: flex;
    align-items: center;
    gap: 6px;
    margin-bottom: 6px;
  }
  .contacts--social { top: 445px; }
  .contact__icon {
    width: 10px;
    height: 10px;
    flex: none;
    fill: var(--text-light);
  }
  .contact__badge {
    width: 9px;
    height: 9px;
    flex: none;
    background: var(--text-light);
  }
</style>
</head>
<body>
<main class="card-sheet">
  <section class="card card--front" aria-label="Card front">
    <div class="brand">
      <span class="brand__mark"></span>
      <span class="brand__name">Vantelo</span>
    </div>
  </section>

  <section class="card card--back" aria-label="Card back">
    <div class="brand">
      <span class="brand__mark"></span>
      <span class="brand__name">Vantelo</span>
    </div>

    <div class="holder">
      <h1 class="holder__name">Daniel Overbeck</h1>
      <p class="holder__role">Entrepreneur</p>
    </div>

    <ul class="contacts">
      <li>
        <svg class="contact__icon" viewBox="0 0 10 10" aria-hidden="true">
          <path d="M2 0.5 L3.6 2.6 L2.8 3.6 Q3.8 5.8 6.4 7.2 L7.4 6.4 L9.5 8 L8.3 9.5 Q1 7.6 0.5 1.7 Z"/>
        </svg>
        <span>07423158871</span>
      </li>
      <li>
        <svg class="contact__icon" viewBox="0 0 10 10" aria-hidden="true">
          <path d="M0.5 2 H9.5 V8 H0.5 Z M1.2 2.6 L5 5.4 L8.8 2.6" fill="none" stroke="#ffffff" stroke-width="1"/>
        </svg>
        <span>doverbeck@vantelo-demo.com</span>
      </li>
    </ul>

    <ul class="contacts contacts--social">
      <li><span class="contact__badge"></span><span>/vantelo</span></li>
      <li><span class="contact__badge"></span><span>/danieloverbeck</span></li>
      <li><span class="contact__badge"></span><span>doverbeck</span></li>
    </ul>
  </section>
</main>
</body>
</html>
```